Business Card and Logo Color Scheme Design Contest

We are starting a new company called Lone Ridge Structural Partners and already have a logo however, the colors for the logo itself are not final and COULD be changed. I'm hoping to move AWAYfrom the gold color in the card and the logo as it seems a bit outdated. What we need help with is to find what our business color scheme will be, and then incorporate those colors into both the logo and the business card design itself. We also want to make sure we are known as "LRS" so in the future we can just refer to ourselves as "LRS" and not Lone Ridge Structural Partners. That being said, I would like to make a slight change to the logo to somehow include the letters "LRS." The logo used in the front of the card design MUST ALSO include the words "Firm No. 64307" within the logo. My vision is for the front of the card to have the information shown in the attached image. For the back of the card, I'm hoping to have something very simple. I'm envisioning a solid color with either the website (www.bridgemarkplans.com) and a simplified version of the logo. I've attached an example but I'm looking for a complete redesign. I'm looking for a slick, modern and simple design.

Industry/Entity Type

Civil Engineer

Contact Information for Business Card

Logo
Firm No. 64307
Daniel Okafor, PE
Chief Operating Officer
Email:dokafor@bridgemarkplans.com
Ph: 936.555.0142 | D: 936.555.0178 | M:210.555.0263
4187 W. Kellingham, Conroe, Texas 77301
www.bridgemarkplans.com

Requirements
Must have
• Logo
Contact Info
Nice to have
• "LRS" Incorporated in the design
Should not have
• The current color scheme

```html
<!DOCTYPE html>
<html lang="en">
<head>
<meta charset="utf-8">
<title>Lone Ridge Structural Partners — Business Card</title>
<link href="https://fonts.googleapis.com/css2?family=Open+Sans:wght@400;600&family=Cinzel:wght@700&display=swap" rel="stylesheet">
<style>
  :root {
    --backdrop: #3a3a3c;
    --card: #141416;
    --ink: #f2f2f2;
    --muted: #b9b9bd;
    --blue: #1f6fd1;
    --red: #d0262c;
    --silver: #c9c9cf;
  }
  * { margin: 0; padding: 0; box-sizing: border-box; }
  html, body { width: 800px; height: 1200px; overflow: hidden; }
  body {
    background: var(--backdrop);
    font-family: "Open Sans", Arial, sans-serif;
    position: relative;
  }
  .card {
    position: absolute;
    left: 50px;
    width: 700px;
    height: 400px;
    background: var(--card);
    overflow: hidden;
    box-shadow: 0 10px 30px rgba(0,0,0,0.45);
  }
  .card--back { top: 130px; }
  .card--front { top: 670px; }

  .brand-mark {
    position: absolute;
    display: flex;
    align-items: center;
    gap: 14px;
  }
  .brand-mark__square {
    width: 22px; height: 22px;
    background: var(--red);
  }
  .brand-mark__name {
    font-family: "Cinzel", Georgia, serif;
    font-weight: 700;
    color: var(--silver);
    letter-spacing: 4px;
  }
  .card--back .brand-mark { left: 300px; top: 120px; }
  .card--back .brand-mark__name { font-size: 64px; }

  .back-url {
    position: absolute;
    left: 60px; top: 330px;
    font-size: 20px;
    letter-spacing: 1px;
    transform: rotate(-8deg);
    transform-origin: left center;
  }
  .back-url__lead { color: var(--blue); }
  .back-url__tail { color: var(--red); }

  .card--front .brand-mark { left: 70px; top: 110px; }
  .card--front .brand-mark__name { font-size: 48px; }

  .firm-number {
    position: absolute;
    left: 300px; top: 358px;
    color: var(--ink);
    font-size: 15px;
    letter-spacing: 0.5px;
  }

  .contact {
    position: absolute;
    left: 340px; top: 62px;
    color: var(--ink);
  }
  .contact__name { color: var(--blue); font-size: 21px; font-weight: 600; }
  .contact__title { font-size: 13px; color: var(--muted); margin-bottom: 18px; }
  .contact__line { font-size: 13.5px; line-height: 1.75; }
  .contact__label { color: var(--blue); font-weight: 600; display: inline-block; width: 22px; }
  .contact__gap { height: 8px; }

  .accent-bands { position: absolute; left: 0; top: 0; }
</style>
</head>
<body>

  <section class="card card--back" aria-label="Card back">
    <div class="brand-mark">
      <span class="brand-mark__square"></span>
      <span class="brand-mark__name">LRS</span>
    </div>
    <p class="back-url"><span class="back-url__lead">www.bridgemark</span><span class="back-url__tail">plans.com</span></p>
  </section>

  <section class="card card--front" aria-label="Card front">
    <svg class="accent-bands" width="700" height="400" viewBox="0 0 700 400" aria-hidden="true">
      <polygon points="0,340 270,340 266,349 0,349" fill="var(--blue)"/>
      <polygon points="272,332 700,312 700,400 230,400" fill="var(--red)"/>
    </svg>

    <div class="brand-mark">
      <span class="brand-mark__square"></span>
      <span class="brand-mark__name">LRS</span>
    </div>
    <p class="firm-number">Firm No. 64307</p>

    <div class="contact">
      <p class="contact__name">Daniel Okafor, PE</p>
      <p class="contact__title">Chief Operating Officer</p>
      <p class="contact__line"><span class="contact__label">P</span>936.555.0142</p>
      <p class="contact__line"><span class="contact__label">D</span>936.555.0178</p>
      <p class="contact__line"><span class="contact__label">M</span>210.555.0263</p>
      <div class="contact__gap"></div>
      <p class="contact__line">dokafor@bridgemarkplans.com</p>
      <p class="contact__line">www.bridgemarkplans.com</p>
      <p class="contact__line">4187 W. Kellingham, Conroe, Texas 77301</p>
    </div>
  </section>

</body>
</html>
```